Real Estate Website

We need a web design for a new site that is focused on real estate listings and information for the Singapore, Malaysian and Australian market.

The web site will have listings of available real estate for sale, past transaction data on real estate, information about neighborhoods where the real estate is located.
Website URL will likely be www.dwellora.net. We are also open to suggestions on site names (assuming URL is available).

We like the simplicity of a similar US site called Vexomi.com - and want to focus on providing a similar "clean" user interface where users can find the information they need. The final design should be user friendly, be visually compelling with a focus on ease of navigation.

Requirements to have at least 5 web pages designed that will display the data as in the attached document for any given territory. We will need to receive
- HTML/CSS/JavaScript, and all images
- any design icons for common objects (e.g. house/home, map, user, agent, trend chart, contact, bathroom, bedroom, garage, furniture, price, ...etc).
Updates

Hi

I just added more details to the brief and committed to pay for the project.
Please review the additional information and submit your final designs by June 14th (or sooner) as we have a deadline to meet. 

Let me know if you have any questions, I will try to be prompt in my responses. 
Thanks.

Target Market(s)

Consumers who are researching real estate to purchase or sell

Industry/Entity Type

Real Estate

Requirements
Must have
• Data in attached document needs to be displayed.

```html
<!DOCTYPE html>
<html lang="en">
<head>
<meta charset="utf-8">
<title>Marlowe Real Estate</title>
<link href="https://fonts.googleapis.com/css2?family=Source+Sans+3:wght@400;600&family=PT+Sans+Narrow:wght@400;700&display=swap" rel="stylesheet">
<style>
:root{
  --blue:#0ea1e6;
  --blue-light:#43bdf0;
  --blue-text:#1d9bd8;
  --grey-dark:#5f5f5f;
  --grey-mid:#9a9a9a;
  --grey-panel:#c4c4c4;
  --line:#dcdcdc;
  --text:#444;
  --white:#fff;
  --footer-top:#8c8c8c;
  --footer-bottom:#5a5a5a;
}
*{box-sizing:border-box;margin:0;padding:0}
html,body{width:1161px;height:1200px;overflow:hidden;background:var(--white);font-family:"Source Sans 3",Arial,sans-serif;color:var(--text)}
.page{position:relative;width:1161px;height:1200px}
.abs{position:absolute}
.topbar{left:0;top:0;width:1161px;height:45px;background:linear-gradient(var(--blue-light) 0 21px,var(--blue) 21px)}
.top-btn{top:11px;height:22px;width:69px;background:var(--white);border-radius:3px;font-size:11px;color:#333;text-align:center;line-height:22px;box-shadow:0 1px 2px rgba(0,0,0,.25)}
.brand{left:160px;top:58px;font-size:36px;color:var(--blue-text);font-weight:400}
.nav{left:413px;top:66px;width:584px;height:27px;display:flex;background:linear-gradient(#8a8a8a,#4a4a4a);border-radius:2px}
.nav span{color:var(--white);font-size:12px;line-height:27px;text-align:center;border-right:1px solid #3a3a3a}
.nav span:last-child{border-right:0}
.search{left:161px;top:113px;width:836px;height:73px;background:linear-gradient(#bdbdbd,#d4d4d4 50%,#bcbcbc);border-radius:2px}
.field{top:20px;height:31px;background:var(--white);border:1px solid #aaa;border-radius:2px;font-size:10.5px;color:var(--blue-text);padding-left:11px;line-height:29px}
.field .drop{position:absolute;right:7px;top:7px;width:16px;height:16px;background:var(--blue);border-radius:3px}
.hero{left:161px;top:204px;width:836px;height:281px;background:linear-gradient(100deg,#4a7fc0 0%,#d9b267 30%,#e8cf95 50%,#d6b170 70%,#6c98cf 100%)}
.hero-arrow{top:112px;width:44px;height:34px;background:rgba(255,255,255,.35)}
.card{top:514px;height:114px;background:var(--grey-dark);border-radius:5px;color:var(--white);box-shadow:0 2px 3px rgba(0,0,0,.3)}
.card h2{position:absolute;left:14px;top:10px;font-family:"PT Sans Narrow",sans-serif;font-weight:400;font-size:18px}
.card p{position:absolute;font-size:10.5px;line-height:13.5px;text-align:justify}
.btn-blue{background:linear-gradient(#3cc0f2,#0a96dc);color:var(--white);border-radius:5px;text-align:center}
.news{left:165px;top:665px;width:520px;height:91px;border:1px solid var(--line);border-radius:5px}
.section-title{font-family:"PT Sans Narrow",sans-serif;color:var(--blue-text);font-size:18px}
.rates{left:705px;top:511px;width:288px;height:244px;background:var(--white);border-radius:5px;box-shadow:0 1px 5px rgba(0,0,0,.3)}
.rates-head{left:4px;top:5px;width:280px;height:33px;border-radius:6px;background:linear-gradient(#4fc4f3,#0c98dd);color:var(--white);font-family:"PT Sans Narrow",sans-serif;font-size:18px;padding-left:13px;line-height:30px}
table{position:absolute;left:9px;top:51px;border-collapse:collapse;font-size:10.5px;color:#333;background:#f2f2f2}
th{background:#434343;color:var(--white);font-weight:400;height:28px;text-align:left;padding-left:10px;border-right:1px solid #888}
td{height:31.5px;padding-left:13px;border-right:1px solid #ccc}
td.num{background:#e3e3e3}
tr:nth-child(2) td{padding-top:18px;height:52px}
.listings{left:164px;top:836px;width:830px;height:209px;border:1px solid var(--line);border-radius:5px}
.thumb{top:14px;width:186px;height:115px;border:1px solid #ccc;padding:4px;background:var(--white)}
.thumb div{width:100%;height:100%}
.cap{top:141px;width:200px;font-size:11.5px;line-height:16px;color:#333}
.more{top:177px;width:75px;height:20px;border-radius:5px;background:linear-gradient(#a8a8a8,#6d6d6d);color:var(--white);font-size:10.5px;text-align:center;line-height:20px}
.sq{top:804px;width:17px;height:18px;background:#5a5a5a}
.footer{left:0;top:1073px;width:1161px;height:127px;background:linear-gradient(var(--footer-top),var(--footer-bottom))}
.footer-links{top:40px;width:100%;text-align:center;font-size:11.5px;color:var(--white)}
.footer-links i{font-style:normal;margin:0 6px}
.copy{top:72px;width:100%;text-align:center;font-size:11.5px;color:var(--white)}
</style>
</head>
<body>
<div class="page">
  <div class="abs topbar"></div>
  <div class="abs top-btn" style="left:838px">Sign Up</div>
  <div class="abs top-btn" style="left:922px">Login</div>

  <div class="abs brand">Marlowe</div>
  <nav class="abs nav">
    <span style="width:97px">Home</span><span style="width:90px">Buy</span><span style="width:96px">Rent</span><span style="width:100px">Mortgage</span><span style="width:93px">Find a Pro</span><span style="width:108px">Contact Us</span>
  </nav>

  <div class="abs search">
    <div class="abs field" style="left:19px;width:190px">Find Properties</div>
    <div class="abs field" style="left:224px;width:190px">Browse by Price<span class="drop"></span></div>
    <div class="abs field" style="left:429px;width:190px">Browse by Region<span class="drop"></span></div>
    <div class="abs field" style="left:633px;width:190px">Browse by Type<span class="drop"></span></div>
  </div>

  <div class="abs hero" role="img" aria-label="Photo of tall cream apartment towers against a blue sky">
    <div class="abs hero-arrow" style="left:0">
      <svg width="44" height="34"><path d="M25 10l-7 7 7 7" stroke="#fff" stroke-width="2.5" fill="none"/></svg>
    </div>
    <div class="abs hero-arrow" style="right:0">
      <svg width="44" height="34"><path d="M19 10l7 7-7 7" stroke="#fff" stroke-width="2.5" fill="none"/></svg>
    </div>
  </div>

  <section class="abs card" style="left:164px;width:256px">
    <h2>Home Finder</h2>
    <p style="left:15px;top:38px;width:130px">Tell us what you are looking for and we'll email you homes that meet your criteria.</p>
    <div class="abs" role="img" aria-label="Hand holding a small model house" style="left:150px;top:22px;width:102px;height:92px;background:radial-gradient(#d8b58c,#8e7660 70%,transparent 72%)"></div>
  </section>
  <div class="abs btn-blue" style="left:180px;top:615px;width:102px;height:24px;font-size:12.5px;line-height:24px;box-shadow:0 1px 2px rgba(0,0,0,.3)">Sign Up Now</div>

  <section class="abs card" style="left:433px;width:255px">
    <h2>Customer Reviews</h2>
    <p style="left:14px;top:38px;width:226px">"From the minute we started talking, Clara Venholt made us feel at ease. She was blowing us away with her determination to get our property out there." Rhea Calloway</p>
    <div class="abs" style="right:18px;top:94px;font-size:10.5px">MORE REVIEWS &gt;&gt;</div>
  </section>

  <section class="abs news">
    <div class="abs section-title" style="left:19px;top:21px">Newsletter Signup</div>
    <div class="abs" style="left:152px;top:16px;width:352px;height:34px;border:1px solid #bbb;border-radius:5px;background:linear-gradient(#fafafa,#e2e2e2);font-size:10.5px;color:#777;padding-left:12px;line-height:32px">Enter your email id</div>
    <div class="abs btn-blue" style="left:437px;top:57px;width:65px;height:26px;font-family:'PT Sans Narrow',sans-serif;font-size:14px;line-height:26px">SIGN UP</div>
  </section>

  <section class="abs rates">
    <div class="abs rates-head">Mortgage Rates</div>
    <table>
      <tr><th style="width:94px">Loan Type</th><th style="width:55px">Rates</th><th style="width:56px">APR</th><th style="width:54px">Points</th><th style="width:11px"></th></tr>
      <tr><td>30 Year fixed</td><td class="num">5%</td><td class="num">5%</td><td class="num">1.000%</td><td></td></tr>
      <tr><td>1 Year ARM</td><td class="num">5.3%</td><td class="num">5.3%</td><td class="num">2.375%</td><td></td></tr>
      <tr><td>5 Year ARM</td><td class="num">8%</td><td class="num">8%</td><td class="num">1.000%</td><td></td></tr>
      <tr><td style="height:42px;vertical-align:top;padding-top:8px">7 Year ARM</td><td class="num" style="vertical-align:top;padding-top:8px">3.6%</td><td class="num" style="vertical-align:top;padding-top:8px">3.6%</td><td class="num" style="vertical-align:top;padding-top:8px">1.375%</td><td></td></tr>
    </table>
  </section>

  <div class="abs section-title" style="left:165px;top:800px">Featured Listings</div>
  <div class="abs sq" style="left:957px"><svg width="17" height="18"><path d="M10 4l-5 5 5 5" stroke="#fff" stroke-width="2" fill="none"/></svg></div>
  <div class="abs sq" style="left:978px"><svg width="17" height="18"><path d="M7 4l5 5-5 5" stroke="#fff" stroke-width="2" fill="none"/></svg></div>

  <section class="abs listings">
    <div class="abs thumb" style="left:12px"><div role="img" aria-label="White villa with terracotta roof" style="background:linear-gradient(#b86a50 0 25%,#e9e4dc 25% 80%,#7a9a3c 80%)"></div></div>
    <div class="abs thumb" style="left:215px"><div role="img" aria-label="Modern house with glass walls and pool" style="background:linear-gradient(#e8e8e8 0 35%,#2e3a30 35% 75%,#6aa840 75%)"></div></div>
    <div class="abs thumb" style="left:420px"><div role="img" aria-label="Patio with wooden lounge chairs" style="background:linear-gradient(135deg,#cfcfcf,#6e5a48 55%,#d8d4cc)"></div></div>
    <div class="abs thumb" style="left:626px"><div role="img" aria-label="Wooden daybed with cushions on a terrace" style="background:linear-gradient(#2f3a2c 0 25%,#d9d6cc 25% 65%,#7d6a50 65%)"></div></div>

    <div class="abs cap" style="left:14px">Featured Property #1 Tenerife, Canary Islands$380,000</div>
    <div class="abs cap" style="left:215px">Featured Property #1 Tenerife, Canary Islands$380,000</div>
    <div class="abs cap" style="left:421px">Featured Property #1 Tenerife, Canary Islands$380,000</div>
    <div class="abs cap" style="left:627px">Featured Property #1 Tenerife, Canary Islands$380,000</div>

    <div class="abs more" style="left:14px">Read More</div>
    <div class="abs more" style="left:217px">Read More</div>
    <div class="abs more" style="left:420px">Read More</div>
    <div class="abs more" style="left:627px">Read More</div>
  </section>

  <footer class="abs footer">
    <div class="abs footer-links">Home<i>|</i>Buy<i>|</i>Rent<i>|</i>Mortgage<i>|</i>Find a Pro<i>|</i>Contact Us</div>
    <div class="abs copy">Copyrights @ 2012 All Rights Reserved</div>
  </footer>
</div>
</body>
</html>
```